Start Up sucht Sticker-, Postkarten- und Herz-Design für Gastgeschenk Seedballs für Hochzeiten
Zielgruppe
Hallo! Wir sind ein Start Up aus dem Saatgutbereich mit verschiedenen Marken. Für unser neues Produkt:
Seedballs in 50er und 100er Abpackungen für Hochzeiten (Gastgeschenke) suchen wir 3 Designs: Zum einen ein Design für den herzförmigen Anhänger (die an die Seedballs in kleinen Organzasäckchen gehangen werden), eine Postkarte die den zu Trauenden einen wunderschönen Tag wünscht und den Sticker der außen auf die Kraftkartonverpackung geklebt wird. Falls die Produkte gut angenommen werden, werden wir eine komplette Faltkartonverpackung erstellen und einsetzen.
Aufgabenstellung
Wir haben für die Marke 'Morgentauer' bereits ein Logo und einige Verpackungen designt. Siehe Anhang. Aber es soll hier vor allem um den Zweck der Gastgeschenke gehen mit Hauptdesign 'Hochzeit'. Logo, Organzasäckchen, Vorlage Herz anbei.
Es solls ich vor allem um das Thema 'Hochzeit' drehen, weniger um die Marke an sich. Das genutzte Papier soll weiß sein, da dies mit den meisten Hochzeitsvorlagen und Dekos zusammen passt.
Als vielleicht passende Fonts kommen: Brittany, Monterchi Serif oder andere in Frage.
Enthalten sind bei den beiden Sets
50er:
50 Seedballs in Kraftpapiertüte mit Sticker
50 Organzasäckchen
50 herzförmige Geschenkanhänger
1x Postkarte für das Ehepaar
100er
100 Seedballs in Kraftpapiertüte mit Sticker
100 Organzasäckchen
100 herzförmige Geschenkanhänger
Folgende Formate sollen genutzt werden:
Postkarte: DIN A6
Herzförmiger Geschenkanhänger: 5x5cm
Sticker für die Verpackung:
50x Seedballs: 8x18cm
100x Seedballs: 10x20cm
Ideen:
Postkarte:
Es soll nur eine allgemeine Postkarte sein die den Trauenden einen wunderschönen Tag und eine wunderschöne Ehe wünscht. Die Rückseite kann ebenfalls designed werden.
Herzförmiger Geschenkanhänger für die Organzasäckchen mit Seedball:
Dort soll etwas wie 'Lasst unsere Liebe wachsen' oder ähnliches stehen, allgemein gehalten. Die Rückseite soll eine ganz kleine Anleitung wie die Seedballs funktionieren enthalten. Siehe Design was es schon gibt.
Das Design soll sich vor allem um Hochzeit und das Thema Gastgeschenk drehen. Außen soll die Anzahl der befindlichen Seedballs stehen (50 bzw. 100) + EAN Code + unsere Kontaktdaten. EAN Codes und Daten werden von uns gestellt. Nutzt bitte zu erst einfache Platzhalter.
Wenn weitere Infos benötigt werden, dann gerne melden. Wir freuen uns auf eure Vorschläge.

```html
<!DOCTYPE html>
<html lang="de">
<head>
<meta charset="utf-8">
<title>Herzanhänger – Lasst unsere Liebe wachsen</title>
<link rel="stylesheet" href="https://fonts.googleapis.com/css2?family=Sacramento&family=Mulish:wght@400;800&display=swap">
<style>
  :root {
    --backdrop: #efefef;
    --paper: #ffffff;
    --ink: #1d1d1d;
    --leaf-deep: #5f7f4a;
    --leaf-soft: #c9d8b4;
    --blush: #e9d9ec;
  }
  html, body {
    margin: 0;
    width: 1200px;
    height: 1200px;
    overflow: hidden;
    background: var(--backdrop);
  }
  .canvas {
    position: relative;
    width: 1200px;
    height: 1200px;
  }
  .tag {
    position: absolute;
  }
  .tag svg {
    position: absolute;
    inset: 0;
    overflow: visible;
  }
  .tag-shape {
    filter: drop-shadow(0 4px 8px rgba(0,0,0,0.18));
  }
  .tag-front { left: 94px; top: 99px; width: 580px; height: 570px; }
  .tag-back  { left: 500px; top: 590px; width: 563px; height: 557px; }

  .motto-line {
    font-family: "Sacramento", cursive;
    font-weight: 400;
    font-size: 92px;
    fill: var(--ink);
  }
  .season-title {
    font-family: "Mulish", sans-serif;
    font-weight: 800;
    font-size: 21px;
    fill: var(--ink);
  }
  .season-range {
    font-family: "Mulish", sans-serif;
    font-weight: 400;
    font-size: 21px;
    fill: var(--ink);
  }
</style>
</head>
<body>
<main class="canvas">

  <section class="tag tag-front">
    <svg class="tag-shape" viewBox="0 0 580 570" width="580" height="570">
      <defs>
        <clipPath id="front-clip">
          <path d="M290 569 L60 330 C-20 240 10 40 150 20 C220 10 265 50 290 95 C315 50 360 10 430 20 C570 40 600 240 520 330 Z"/>
        </clipPath>
        <radialGradient id="leaf-green" cx="50%" cy="50%" r="50%">
          <stop offset="0" stop-color="#6f8f58" stop-opacity="0.85"/>
          <stop offset="0.55" stop-color="#a9c08f" stop-opacity="0.55"/>
          <stop offset="1" stop-color="#dfe9d2" stop-opacity="0"/>
        </radialGradient>
        <radialGradient id="leaf-blush" cx="50%" cy="50%" r="50%">
          <stop offset="0" stop-color="#e6d3ea" stop-opacity="0.8"/>
          <stop offset="1" stop-color="#f4ecf5" stop-opacity="0"/>
        </radialGradient>
      </defs>
      <path d="M290 569 L60 330 C-20 240 10 40 150 20 C220 10 265 50 290 95 C315 50 360 10 430 20 C570 40 600 240 520 330 Z" fill="var(--paper)"/>
      <g clip-path="url(#front-clip)">
        <g role="img" aria-label="Aquarell-Blätterranke über dem Spruch">
          <ellipse cx="300" cy="125" rx="270" ry="75" fill="url(#leaf-green)"/>
          <ellipse cx="260" cy="140" rx="110" ry="45" fill="url(#leaf-blush)"/>
        </g>
        <g role="img" aria-label="Aquarell-Blätterranke unter dem Spruch">
          <ellipse cx="280" cy="420" rx="240" ry="70" fill="url(#leaf-green)"/>
          <ellipse cx="320" cy="410" rx="100" ry="40" fill="url(#leaf-blush)"/>
        </g>
        <rect x="69" y="175" width="437" height="196" fill="var(--paper)"/>
      </g>
      <text class="motto-line" x="90" y="269" textLength="257" lengthAdjust="spacingAndGlyphs">Lasst unsere</text>
      <text class="motto-line" x="193" y="342" textLength="292" lengthAdjust="spacingAndGlyphs">Liebe wachsen!</text>
    </svg>
  </section>

  <section class="tag tag-back">
    <svg class="tag-shape" viewBox="0 0 563 557" width="563" height="557">
      <defs>
        <clipPath id="back-clip">
          <path d="M281 556 L58 322 C-18 235 10 40 145 20 C215 10 258 48 281 92 C305 48 348 10 418 20 C553 40 581 235 505 322 Z"/>
        </clipPath>
        <radialGradient id="leaf-green-b" cx="50%" cy="50%" r="50%">
          <stop offset="0" stop-color="#6f8f58" stop-opacity="0.8"/>
          <stop offset="0.55" stop-color="#b3c89a" stop-opacity="0.5"/>
          <stop offset="1" stop-color="#e3ecd7" stop-opacity="0"/>
        </radialGradient>
      </defs>
      <path d="M281 556 L58 322 C-18 235 10 40 145 20 C215 10 258 48 281 92 C305 48 348 10 418 20 C553 40 581 235 505 322 Z" fill="var(--paper)"/>
      <g clip-path="url(#back-clip)">
        <g role="img" aria-label="Aquarell-Blätter oben links">
          <ellipse cx="110" cy="75" rx="120" ry="70" fill="url(#leaf-green-b)"/>
        </g>
        <g role="img" aria-label="Aquarell-Blätter oben rechts">
          <ellipse cx="480" cy="95" rx="110" ry="80" fill="url(#leaf-green-b)"/>
        </g>
      </g>
    </svg>

    <svg class="care-guide" viewBox="0 0 563 557" width="563" height="557">
      <g class="care-icons" fill="none" stroke="var(--ink)" stroke-width="2.6" stroke-linecap="round" stroke-linejoin="round" aria-hidden="true">
        <circle cx="276" cy="113" r="39"/>
        <g fill="var(--ink)" stroke="none">
          <circle cx="264" cy="96" r="2.6"/><circle cx="285" cy="92" r="2.6"/>
          <circle cx="253" cy="110" r="2.6"/><circle cx="271" cy="113" r="2.6"/>
          <circle cx="291" cy="112" r="2.6"/><circle cx="260" cy="126" r="2.6"/>
          <circle cx="280" cy="131" r="2.6"/><circle cx="296" cy="126" r="2.6"/>
        </g>
        <path d="M279 166 V196 M272 188 L279 196 L286 188"/>
        <path d="M105 275 L112 222 L120 215 M128 275 L118 225 M112 222 a6 6 0 1 0 1 0"/>
        <path d="M142 215 C130 228 130 245 142 250 C154 245 154 228 142 215 Z M142 250 V277"/>
        <rect x="188" y="250" width="68" height="27"/>
        <path d="M188 260 H256"/>
        <path d="M203 250 V228 M222 250 V228 M241 250 V228"/>
        <circle cx="203" cy="222" r="6"/><circle cx="222" cy="222" r="6"/><circle cx="241" cy="222" r="6"/>
        <path d="M295 232 H345 V242 H295 Z M299 242 L305 277 H335 L341 242"/>
        <path d="M320 232 C308 228 306 214 314 214 C318 214 320 222 320 232 C320 222 322 214 326 214 C334 214 332 228 320 232"/>
        <path d="M386 277 H460"/>
        <path d="M424 277 V230 M424 250 L412 240 M424 245 L436 235"/>
        <ellipse cx="424" cy="236" rx="22" ry="30"/>
        <ellipse cx="393" cy="262" rx="9" ry="12"/>
        <path d="M393 277 V262"/>
        <path d="M81 313 H470" stroke-width="2"/>
        <path d="M190 346 C200 341 206 340 214 344 H236 C242 344 242 352 236 352 H218 M236 352 C244 352 244 360 236 360 H202 C196 360 192 358 190 356"/>
        <circle cx="216" cy="382" r="8" fill="var(--ink)" stroke="none"/>
        <path d="M214 436 V464 M195 466 C200 458 228 458 233 466 Z"/>
        <path d="M214 441 C210 428 198 424 188 426 C192 438 204 442 214 441 Z"/>
        <path d="M214 441 C218 428 230 424 240 426 C236 438 224 442 214 441 Z"/>
      </g>
      <text class="season-title" x="265" y="354">Aussaat</text>
      <text class="season-range" x="265" y="389">Apr. - Juni</text>
      <text class="season-title" x="265" y="436">Blüte</text>
      <text class="season-range" x="265" y="469">Juli - Okt.</text>
    </svg>
  </section>

</main>
</body>
</html>
```